Letterhead and Corporate Stationary Design Project

I would like the following designed:
1. Corporate Letterhead
2. Compliment Slips
3. Business Cards(2)

I have attached word document that outlines the text to be contained for all 3. The logo is fine as is and can be used in the design.
I only need letterhead to be designed for contest, the successful applicant can desisgn other 2 items after being awarded the job

Target Market(s)

Information Technology

Industry/Entity Type

Business

Requirements
Must have
• Border around entire letter that matches colours in logo
Clearly identifiable letterhead and footer
Nice to have
• Watermark

```html
<!DOCTYPE html>
<html lang="en">
<head>
<meta charset="utf-8">
<title>Corvane Business Solutions — Letterhead</title>
<link href="https://fonts.googleapis.com/css2?family=Arimo:wght@400;700&family=Carlito:wght@400&family=Great+Vibes&display=swap" rel="stylesheet">
<style>
  :root {
    --brand-blue: #1a9ad6;
    --brand-navy: #1d4e8f;
    --text-dark: #111111;
    --text-muted: #8a8a8a;
    --frame-grey: #b5b5b5;
    --watermark-blue: #d6ebf8;
    --watermark-slate: #dde3ec;
    --paper: #ffffff;
  }
  * { box-sizing: border-box; margin: 0; padding: 0; }
  html, body {
    width: 1000px; height: 1200px; overflow: hidden; background: var(--paper);
  }
  .letterhead {
    position: relative; width: 1000px; height: 1200px;
    background: var(--paper);
    border: 1px solid var(--frame-grey);
    font-family: "Arimo", Arial, sans-serif;
    color: var(--text-dark);
    overflow: hidden;
  }
  .brand {
    position: absolute; left: 58px; top: 62px;
    display: flex; align-items: center; gap: 14px;
  }
  .brand-dot {
    width: 46px; height: 46px; border-radius: 50%;
    background: var(--brand-blue);
  }
  .brand-name {
    font-family: "Arimo", Arial, sans-serif;
    font-weight: 700; font-size: 30px; line-height: 1.1;
    color: var(--brand-blue);
  }
  .contact-block {
    position: absolute; left: 793px; top: 34px;
    border-left: 2px solid var(--brand-blue);
    padding-left: 19px;
    font-family: "Carlito", Calibri, sans-serif;
    font-size: 9.5px; line-height: 12.4px;
    color: var(--text-muted);
  }
  .contact-label { color: var(--brand-blue); }
  .watermark {
    position: absolute; left: 500px; top: 680px;
    width: 480px; height: 440px;
    background: radial-gradient(ellipse at 45% 35%, var(--watermark-blue) 0%, rgba(221,227,236,0.6) 45%, rgba(255,255,255,0) 72%);
  }
  .salutation {
    position: absolute; left: 96px; top: 222px;
    font-size: 18px;
  }
  .letter-body {
    position: absolute; left: 171px; top: 261px; width: 745px;
    font-size: 17.2px; line-height: 21.6px;
  }
  .letter-body p { margin-bottom: 21.6px; }
  .signature {
    position: absolute; left: 90px; top: 928px;
    font-family: "Great Vibes", cursive;
    font-size: 58px; line-height: 1;
  }
  .signatory-title {
    position: absolute; left: 119px; top: 998px;
    font-size: 18px;
  }
  .footer-band {
    position: absolute; left: 0; right: 0; top: 1154px; height: 30px;
    background: var(--brand-blue);
    display: flex; align-items: center; justify-content: center; gap: 30px;
    font-family: "Carlito", Calibri, sans-serif;
    font-size: 16.5px; color: var(--paper);
  }
  .footer-sep {
    width: 9px; height: 9px; border-radius: 50%; background: var(--paper);
  }
</style>
</head>
<body>
  <main class="letterhead">
    <header>
      <div class="brand">
        <span class="brand-dot"></span>
        <span class="brand-name">corvane<br>Business Solutions</span>
      </div>
      <address class="contact-block" style="font-style:normal">
        Corvane Business Solutions<br>
        Harbour Court<br>
        22 Mill Street<br>
        Dundalk<br>
        Co. Louth<br>
        Ireland<br>
        <span class="contact-label">Tel:</span> + 353 42 9155104<br>
        <span class="contact-label">Web:</span> www.corvane.ie
      </address>
    </header>

    <div class="watermark" role="img" aria-label="Faint brand watermark area"></div>

    <p class="salutation">Dear Sir / Madam,</p>

    <section class="letter-body">
      <p>Lorem ipsum dolor sit amet, consectetur adipisicing elit, sed do eiusmod tempor labore et olore magna aliqua. Ut enim ad minim veniam, quis nostrud exercitation ullamco laboris nisi ut aliquip ex ea commodo consequa.Lorem ipsum dolor sit amet, nsectetur adipisicing elit, sed do eiusmod tempor incididunt ut labore et dolore magna aliqua. Ut enim ad minim veniam, quis.</p>
      <p>Lorem ipsum dolor sit amet, consectetur adipisicing elit, sed do eiusmod tempor labore et dolore magna aliqua. Ut enim ad minim veniam, quis nostrud exercitation ullamco laboris nisi ut aliquip ex ea commodo consequa.Lorem ipsum dolor sit amet, nsectetur adipisicing elit, sed do eiusmod tempor incididunt ut labore et dolore magna aliqua. Ut enim ad minim veniam, quis.</p>
      <p>Lorem ipsum dolor sit amet, consectetur adipisicing elit, sed do eiusmod tempor labore et dolore magna aliqua. Ut enim ad minim veniam, quis nostrud exercitation ullamco laboris nisi ut aliquip ex ea commodo consequa.Lorem ipsum dolor sit amet, nsectetur adipisicing elit, sed do eiusmod tempor incididunt ut labore et dolore magna aliqua. Ut enim ad minim veniam, quis.</p>
      <p>Lorem ipsum dolor sit amet, consectetur adipisicing elit, sed do eiusmod tempor labore et dolore magna aliqua. Ut enim ad minim veniam, quis nostrud exercitation ullamco laboris nisi ut aliquip ex ea commodo consequa.Lorem ipsum dolor sit amet, nsectetur adipisicing elit, sed do eiusmod tempor incididunt ut labore et dolore magna aliqua. Ut enim ad minim veniam, quis.</p>
      <p>Lorem ipsum dolor sit amet, consectetur adipisicing elit, sed do eiusmod tempor labore et dolore magna aliqua. Ut enim ad minim veniam, quis nostrud exercitation ullamco laboris nisi ut aliquip ex ea commodo consequa.Lorem ipsum dolor sit amet, nsectetur adipisicing elit, sed do eiusmod tempor incididunt ut labore et dolore magna aliqua. Ut enim ad minim veniam, quis.</p>
    </section>

    <p class="signature">Your Name</p>
    <p class="signatory-title">Company Director</p>

    <footer class="footer-band">
      <span>Corvane Business Solutions Limited</span>
      <span class="footer-sep"></span>
      <span>Company Registration 517394</span>
      <span class="footer-sep"></span>
      <span>VAT No IE7391046K</span>
    </footer>
  </main>
</body>
</html>
```